Landing Page for Bathroom Remodeling Webpage - Desktop and Mobile

I am looking for some help designing the "above the fold" area for my bathroom remodeling service page. Looking for something a little different than the rest. Typically remodeling companies just put a nice picture of a bathroom remodel but I would like to do something a little different / more creative. Below is a link to the current wireframe we are working on.
Current website is located at plumvantaridge.com
Again the biggest thing I am looking for is a design for the very top section but would love help on the rest of the page as well. You will see by viewing the link below the type of information we are looking to include on the page:
PLEASE DO INCLUDE WHAT THE MOBILE VERSION WOULD LOOK LIKE AS WELL.
Wireframe:
https://boards.quillmerra.com/view/3f8a1b2c-90de-4e7a-b5c1-aa62d09e1f35-418k/
There are also comments in the link above you can read as well.
We like the idea of something interactive such as this...
https://pixorvale.com/shots/5192746-Glenhart-Scooter-Store-Animation
Attached is also the logo we want to use going forward
Target Market(s)
Residential homeowners, 30 years old+ with professional careers
Number of Pages Required
1 page
Look and feel
Each slider illustrates characteristics of the customer's brand and the style your logo design should communicate.

```html
<!DOCTYPE html>
<html lang="en">
<head>
<meta charset="utf-8">
<title>Plumvanta – Bathroom Remodeling</title>
<link href="https://fonts.googleapis.com/css2?family=Libre+Baskerville:wght@400;700&family=Poppins:wght@400;500;600;700&family=Roboto+Condensed:wght@400;500&display=swap" rel="stylesheet">
<style>
:root{
  --navy:#0c3268;
  --navy-dark:#082653;
  --red:#d23333;
  --ink:#222;
  --muted:#666;
  --line:#d9dde4;
  --white:#fff;
  --serif:'Libre Baskerville',serif;
  --sans:'Poppins',sans-serif;
  --cond:'Roboto Condensed',sans-serif;
}
*{box-sizing:border-box;margin:0;padding:0}
html,body{width:1200px;height:5034px;overflow:hidden}
body{font-family:var(--sans);color:var(--ink);background:var(--white);position:relative}
section,header,footer{position:absolute;left:0;width:1200px}
.abs{position:absolute}
.brand{display:flex;align-items:center;gap:10px;font-family:var(--sans);font-weight:700;color:var(--white);letter-spacing:1px}
.brand .mark{width:22px;height:22px;border-radius:50%;background:var(--white)}
.h-serif{font-family:var(--serif);font-weight:700}
.btn{display:inline-block;font-family:var(--sans);font-weight:600;text-transform:uppercase;font-size:14px;color:var(--white);background:var(--navy);text-align:center}
.photo{position:absolute}

/* header / hero */
.hero{top:0;height:675px}
.hero .side{left:0;top:0;width:258px;height:675px;background:var(--navy)}
.hero .side .brand{position:absolute;left:60px;top:18px;font-size:22px}
.hero .contact-vert{position:absolute;left:56px;top:445px;transform:rotate(-90deg);transform-origin:left top;color:var(--white);font-size:15px;white-space:nowrap}
.hero .contact-vert b{font-size:20px;font-weight:600;text-decoration:underline}
.nav{position:absolute;left:626px;top:30px;display:flex;gap:24px;font-size:13px;color:var(--muted)}
.nav .on{color:var(--navy);font-weight:500}
.estimate{position:absolute;left:1013px;top:0;width:187px;height:78px;background:var(--red);color:var(--white);text-align:center;padding-top:16px;font-size:13px;line-height:22px}
.estimate b{font-size:15px;font-weight:600;letter-spacing:.5px}
.hero-photo{left:143px;top:78px;width:938px;height:518px;background:linear-gradient(120deg,#e8ebee 0%,#d4d8dc 40%,#f2f2f2 70%,#a9aeb3 100%)}
.hero h1{position:absolute;left:238px;top:195px;font-family:var(--serif);font-weight:700;font-size:56px;line-height:70px;color:var(--red)}
.hero .lede{position:absolute;left:238px;top:340px;width:460px;font-size:15px;line-height:24px;color:#222}
.hero .cta{position:absolute;left:236px;top:404px;width:142px;height:36px;line-height:36px}
.social{position:absolute;left:1105px;top:222px;display:flex;flex-direction:column;gap:14px}
.social span{width:34px;height:34px;border-radius:50%;background:#eceef2;display:block;position:relative}
.social span::after{content:"";position:absolute;left:11px;top:11px;width:12px;height:12px;border-radius:50%}
.social span:nth-child(1)::after{background:#1f3f8a}
.social span:nth-child(2)::after{background:#2aa3e8}
.social span:nth-child(3)::after{background:#e02020}
.social span:nth-child(4)::after{background:#e03a6a}
.strip{position:absolute;left:258px;top:596px;width:942px;height:79px;background:var(--red);color:var(--white);font-size:15px;font-weight:500}
.strip p{position:absolute;left:38px;top:30px}
.strip .btn{position:absolute;left:746px;top:27px;width:136px;height:36px;line-height:36px;background:var(--navy)}

/* about */
.about{top:675px;height:527px}
.about .p1{left:154px;top:75px;width:358px;height:300px;background:linear-gradient(135deg,#c9d3e0,#8fa0b8 50%,#e5e9ee)}
.about .p2{left:260px;top:257px;width:302px;height:197px;background:linear-gradient(135deg,#cfc6bc,#7e7670 55%,#ece8e2);border:4px solid #fff}
.about .txt{position:absolute;left:628px;top:88px;width:420px}
.eyebrow{font-size:15px;color:#333}
.about h2{font-size:23px;line-height:34px;color:var(--navy);margin:12px 0 18px}
.about p{font-size:12px;line-height:20px;color:var(--muted);margin-bottom:12px}
.more{display:flex;align-items:center;gap:14px;font-size:13px;font-weight:600;color:var(--navy);margin-top:18px}
.more i{width:36px;height:36px;border-radius:50%;border:1.5px solid var(--red);color:var(--red);font-style:normal;text-align:center;line-height:32px;font-size:22px;font-weight:300}

/* materials */
.materials{top:1202px;height:498px;background:var(--navy);color:var(--white);text-align:center}
.sec-title{font-family:var(--serif);font-weight:700;font-size:22px}
.sec-sub{font-size:12px;line-height:21px;margin:18px auto 0}
.materials .sec-title{margin-top:68px}
.materials .sec-sub{width:560px}
.cards{position:absolute;left:135px;top:180px;display:flex;gap:31px}
.mcard{width:210px;height:246px;background:var(--white);border-radius:4px;text-align:left;padding:22px 20px;color:var(--ink)}
.mcard .ic{width:64px;height:64px;border-radius:50%;border:2px solid var(--navy);display:flex;align-items:center;justify-content:center}
.mcard h3{font-family:var(--cond);font-weight:500;font-size:17px;color:var(--navy);margin:18px 0 14px}
.mcard li{list-style:none;font-size:12px;color:var(--muted);line-height:30px;padding-left:18px;position:relative}
.mcard li::before{content:"";position:absolute;left:2px;top:10px;width:8px;height:4px;border-left:2px solid var(--navy);border-bottom:2px solid var(--navy);transform:rotate(-45deg)}

/* projects */
.projects{top:1700px;height:544px;text-align:center}
.projects .sec-title{margin-top:82px;color:var(--navy)}
.proj{position:absolute;top:145px;width:323px;height:262px}
.proj.a{left:60px;background:linear-gradient(160deg,#3f6aa0,#26497c)}
.proj.b{left:412px;background:linear-gradient(160deg,#6d6a66,#c9c2b8 60%,#e7e2da)}
.proj.c{left:764px;background:linear-gradient(160deg,#f0ede9,#c8a8ac 60%,#e3dcd6)}
.proj.a .frame{position:absolute;inset:12px;border:1.5px solid rgba(255,255,255,.7)}
.proj.a .cap{position:absolute;left:0;right:0;top:88px;color:var(--white);font-family:var(--cond);font-size:16px;line-height:28px}
.projects .btn{position:absolute;left:533px;top:430px;width:134px;height:37px;line-height:37px;font-size:13px}

/* pricing */
.pricing{top:2244px;height:674px;background:var(--red);color:var(--white);text-align:center}
.pricing .sec-title{margin-top:74px}
.pricing .sec-sub{width:600px}
.plan{position:absolute;top:170px;width:300px;height:413px;background:var(--white);color:var(--ink);overflow:hidden}
.plan .head{height:166px;background:var(--navy);color:var(--white);padding-top:22px}
.plan h3{font-family:var(--cond);font-weight:400;font-size:20px}
.plan .d{font-size:12px;line-height:20px;width:240px;margin:10px auto 0}
.plan .price{font-family:var(--cond);font-weight:500;font-size:26px;margin-top:12px}
.plan ul{text-align:left;padding:24px 0 0 20px}
.plan li{list-style:none;font-size:12px;color:var(--muted);line-height:22.7px;padding-left:22px;position:relative}
.plan li::before{content:"»";position:absolute;left:0;top:-1px;color:var(--navy);font-size:15px}
.plan.p1{left:113px}.plan.p2{left:450px}.plan.p3{left:787px}
.ribbon{position:absolute;left:-30px;top:22px;width:130px;background:var(--white);color:var(--navy);transform:rotate(-45deg);font-size:12px;line-height:14px;padding:3px 0;font-weight:500}

/* faq */
.faq{top:2918px;height:485px}
.faq h2{position:absolute;left:60px;top:78px;font-size:22px;color:var(--navy)}
.faq .items{position:absolute;left:60px;top:126px;width:470px}
.q{height:37px;border-radius:19px;border:1px solid var(--line);font-size:12px;padding:0 16px;display:flex;align-items:center;justify-content:space-between;margin-bottom:16px}
.q b{font-weight:400;font-size:22px;color:var(--navy);font-weight:300}
.q.open{background:var(--navy);color:var(--white);border-color:var(--navy);margin-bottom:12px}
.q.open b{color:var(--white)}
.faq .ans{font-size:12px;line-height:20px;color:var(--muted);margin-bottom:20px}
.faq .back{left:778px;top:183px;width:313px;height:226px;background:#ccd7e2}
.faq .pic{left:739px;top:72px;width:316px;height:300px;background:linear-gradient(180deg,#e8e6e1,#b9b6b0 55%,#d9d4cc)}

/* schedule */
.schedule{top:3403px;height:510px;background:var(--navy);color:var(--white);text-align:center}
.schedule .sec-title{margin-top:78px}
.tabs{position:absolute;left:284px;top:122px;display:flex;gap:28px}
.tabs span{height:34px;line-height:34px;border-radius:17px;background:#3a5b8c;font-size:13px}
.steps{position:absolute;left:140px;top:210px;display:flex;gap:0}
.step{width:310px;margin-right:17px}
.step .ring{width:120px;height:120px;border-radius:50%;border:2px dashed rgba(255,255,255,.6);margin:0 auto;display:flex;align-items:center;justify-content:center}
.step .ring span{width:94px;height:94px;border-radius:50%;background:var(--white);display:flex;align-items:center;justify-content:center}
.step h3{font-family:var(--cond);font-weight:400;font-size:17px;margin:20px 0 14px}
.step p{font-size:12px;line-height:20px;color:#c8d3e4;width:270px;margin:0 auto}

/* articles */
.articles{top:3913px;height:591px}
.articles .intro{position:absolute;left:104px;top:120px;width:270px}
.articles .intro .h-serif{font-size:22px;color:var(--navy)}
.articles .intro h2{font-size:25px;font-weight:600;line-height:34px;margin:10px 0 16px;letter-spacing:.5px}
.articles .intro p{font-size:12px;line-height:20px;color:var(--muted)}
.articles .intro a{display:block;margin-top:18px;font-size:13px;font-weight:600;color:var(--navy);text-decoration:none}
.post{position:absolute;top:76px;width:300px}
.post .img{height:240px}
.post.a{left:458px}.post.a .img{background:linear-gradient(150deg,#ececec,#b9b3ad 60%,#f4f2ef)}
.post.b{left:796px}.post.b .img{background:linear-gradient(150deg,#d9d2c5,#9aa69a 50%,#ece6da)}
.post .meta{display:flex;gap:24px;font-size:12px;color:var(--muted);margin:22px 0 26px;align-items:center}
.post .meta span{display:flex;align-items:center;gap:12px}
.post .meta i{width:24px;height:24px;border:1px solid var(--line);display:inline-block;border-radius:3px}
.post h3{font-family:var(--cond);font-weight:400;font-size:16px;line-height:24px}

/* footer */
.footer{top:4504px;height:530px;background:var(--red);color:var(--white)}
.footer .sec-title{position:absolute;left:0;width:1200px;text-align:center;top:54px}
.contact{position:absolute;top:128px;display:flex;align-items:center;gap:18px}
.contact .c{width:84px;height:84px;border-radius:50%;background:var(--white);border:4px solid #f2c1c1;display:flex;align-items:center;justify-content:center}
.contact small{font-family:var(--cond);font-size:18px;display:block}
.contact b{font-family:var(--cond);font-weight:500;font-size:29px}
.contact.l{left:155px}.contact.r{left:800px}
.footer hr{position:absolute;left:60px;top:207px;width:1080px;border:0;border-top:1px solid rgba(255,255,255,.4)}
.footer .brand{position:absolute;left:60px;top:268px;font-size:27px}
.footer .brand .mark{width:34px;height:34px}
.fsocial{position:absolute;left:60px;top:328px;display:flex;gap:14px}
.fsocial span{width:32px;height:32px;border-radius:50%;background:var(--white)}
.col{position:absolute;top:268px}
.col h4{font-family:var(--cond);font-weight:500;font-size:19px;margin-bottom:8px}
.col li{list-style:none;font-size:12px;line-height:22.5px}
.col.s{left:432px}.col.a{left:803px}
.copy{position:absolute;left:0;top:510px;width:1200px;height:20px;background:var(--navy);text-align:center;font-size:11px;line-height:20px}
</style>
</head>
<body>

<header class="hero">
  <div class="abs side">
    <div class="brand"><span class="mark"></span>PLUMVANTA</div>
    <div class="contact-vert">Contact Us At <b>555-014-2290</b></div>
  </div>
  <div class="photo hero-photo" role="img" aria-label="Bright modern bathroom with grey vanity, vessel sink, wall mirror and pendant light"></div>
  <nav class="nav"><span class="on">Home</span><span>Services</span><span>Gallery</span><span>Blog</span><span>About</span><span>Contact</span></nav>
  <div class="estimate">GET AN ESTIMATE<br><b>555-014-2290</b></div>
  <h1>We Are Always<br>Ready for You</h1>
  <p class="lede">It's where you start and end your day. A bathroom remodel will make sure it starts and ends right.</p>
  <a class="btn cta">Contact Us</a>
  <div class="social"><span></span><span></span><span></span><span></span></div>
  <div class="strip">
    <p>Schedule a free in home consultation Via Our Online Appointment Scheduling System</p>
    <a class="btn">Schedule</a>
  </div>
</header>

<section class="about">
  <div class="photo p1" role="img" aria-label="Bathroom with round mirror, blue cabinets and glass shower"></div>
  <div class="photo p2" role="img" aria-label="Bathroom with freestanding tub and dark walls"></div>
  <div class="txt">
    <div class="eyebrow">About Company</div>
    <h2 class="h-serif">Bathroom Remodeling Made<br>Simple</h2>
    <p>Lorem Ipsum is simply dummy text of the printing and typesetting industry. Lorem Ipsum has been the industry's standard dummy text ever since the 1500s,</p>
    <p>t is a long established fact that a reader will be distracted by the readable content of a page when looking at its layout. The point of using Lorem Ipsum is that it has a more-or-less normal distribution of letters, as opposed to using 'Content here, content here', making it look like readable English.</p>
    <div class="more"><i>+</i>SHOW ME MORE</div>
  </div>
</section>

<section class="materials">
  <h2 class="sec-title">Material Selections</h2>
  <p class="sec-sub">For your bathroom remodel there will be material selections you will have to make. Use the lists below to get an idea of some of the options.</p>
  <div class="cards">
    <div class="mcard"><div class="ic"><svg width="30" height="34" viewBox="0 0 30 34"><rect x="5" y="2" width="20" height="30" rx="2" fill="none" stroke="#0c3268" stroke-width="2"/><rect x="10" y="8" width="10" height="8" fill="#d23333"/><line x1="10" y1="22" x2="20" y2="22" stroke="#0c3268" stroke-width="2"/></svg></div><h3>Electrical</h3><ul><li>Light Fixtures</li><li>Heated Floor</li><li>Outlets</li></ul></div>
    <div class="mcard"><div class="ic"><svg width="34" height="30" viewBox="0 0 34 30"><path d="M3 14h28v4a8 8 0 0 1-8 8H11a8 8 0 0 1-8-8z" fill="none" stroke="#0c3268" stroke-width="2"/><path d="M7 14V5a3 3 0 0 1 6 0" fill="none" stroke="#d23333" stroke-width="2"/></svg></div><h3>Plumbing</h3><ul><li>Vanity Fixtures</li><li>Shower Fixtures</li><li>Toilet</li></ul></div>
    <div class="mcard"><div class="ic"><svg width="32" height="32" viewBox="0 0 32 32"><path d="M16 2 30 16 16 30 2 16z" fill="none" stroke="#0c3268" stroke-width="2"/><path d="M16 9 23 16 16 23 9 16z" fill="#d23333"/></svg></div><h3>Tile &amp; Flooring</h3><ul><li>Shower Wall Tile</li><li>Shower Floor Tile</li><li>Bathroom Flooring</li></ul></div>
    <div class="mcard"><div class="ic"><svg width="32" height="30" viewBox="0 0 32 30"><rect x="3" y="4" width="26" height="22" rx="2" fill="none" stroke="#0c3268" stroke-width="2"/><rect x="8" y="9" width="7" height="6" fill="#d23333"/><rect x="17" y="9" width="7" height="6" fill="none" stroke="#0c3268" stroke-width="1.5"/></svg></div><h3>Finishes</h3><ul><li>Trim</li><li>Mirrors &amp; Towel Bars</li><li>Cabinetry &amp; Counter Tops</li></ul></div>
  </div>
</section>

<section class="projects">
  <h2 class="sec-title">Get Inspired By Similar Projects</h2>
  <div class="proj a" role="img" aria-label="Blue-tinted bathroom remodel project"><div class="frame"></div><div class="cap">Bathroom Remodeling<br>In Woodland Hills , CA</div></div>
  <div class="proj b" role="img" aria-label="Bathroom with tub, shutters and marble vanity"></div>
  <div class="proj c" role="img" aria-label="Bathroom with pink vanity and round mirrors"></div>
  <a class="btn">See More</a>
</section>

<section class="pricing">
  <h2 class="sec-title">Pricing Packages</h2>
  <p class="sec-sub">Pricing for bathroom remodels can vary dramatically. Below you will find typical services with the varying cost levels.</p>
  <div class="plan p1"><div class="head"><h3>Minor Finish</h3><p class="d">Lorem Ipsum is simply dummy text of the printing and</p><div class="price">$299.00</div></div><ul><li>Shower Fixtures</li><li>Vanity Fixtures</li><li>Mirrors / Towel Bars</li><li>Tile</li><li>Cabinetry</li><li>Counter Tops</li><li>Re-Route Plumbing / Electrica</li><li>Move Walls</li></ul></div>
  <div class="plan p2"><div class="ribbon">Best<br>Value</div><div class="head"><h3>Moderate Finish</h3><p class="d">Lorem Ipsum is simply dummy text of the printing and</p><div class="price">$299.00</div></div><ul><li>Shower Fixtures</li><li>Vanity Fixtures</li><li>Mirrors / Towel Bars</li><li>Tile</li><li>Cabinetry</li><li>Counter Tops</li><li>Re-Route Plumbing / Electrica</li><li>Move Walls</li></ul></div>
  <div class="plan p3"><div class="head"><h3>Minor Finish</h3><p class="d">Lorem Ipsum is simply dummy text of the printing and</p><div class="price">$299.00</div></div><ul><li>Shower Fixtures</li><li>Vanity Fixtures</li><li>Mirrors / Towel Bars</li><li>Tile</li><li>Cabinetry</li><li>Counter Tops</li><li>Re-Route Plumbing / Electrica</li><li>Move Walls</li></ul></div>
</section>

<section class="faq">
  <h2 class="h-serif">Frequently Asked Questions</h2>
  <div class="items">
    <div class="q open">How much does a bathroom remodel cost?<b>–</b></div>
    <p class="ans">It's the question that is top of mind for all customers and they usually do not like the typical "it varies" response. Unfortunately, it is a tough question to answer. If the remodel is a minor upgrade you could be</p>
    <div class="q">How Will Long Take It?<b>+</b></div>
    <div class="q">Do You Pull Permits?<b>+</b></div>
    <div class="q">Are You Licence And Insured?<b>+</b></div>
  </div>
  <div class="photo back"></div>
  <div class="photo pic" role="img" aria-label="White shiplap bathroom hallway with chandelier and tub"></div>
</section>

<section class="schedule">
  <h2 class="sec-title">Schedule Your Free Consultation Today!</h2>
  <div class="tabs"><span style="width:190px">Choose Appointment</span><span style="width:190px">Your Info</span><span style="width:190px">Confirmation</span></div>
  <div class="steps">
    <div class="step"><div class="ring"><span><svg width="46" height="42" viewBox="0 0 46 42"><rect x="3" y="6" width="34" height="30" rx="3" fill="none" stroke="#0c3268" stroke-width="2.5"/><line x1="3" y1="14" x2="37" y2="14" stroke="#0c3268" stroke-width="2.5"/><circle cx="34" cy="30" r="9" fill="#fff" stroke="#0c3268" stroke-width="2.5"/><path d="M34 25v5h4" fill="none" stroke="#0c3268" stroke-width="2"/></svg></span></div><h3>Schedule an Appointment Today</h3><p>View our calendar on the left and pick an oppointment time that works best for you.</p></div>
    <div class="step"><div class="ring"><span><svg width="40" height="44" viewBox="0 0 40 44"><rect x="6" y="5" width="26" height="35" rx="3" fill="none" stroke="#0c3268" stroke-width="2.5"/><line x1="12" y1="16" x2="26" y2="16" stroke="#0c3268" stroke-width="2"/><line x1="12" y1="23" x2="26" y2="23" stroke="#0c3268" stroke-width="2"/><line x1="12" y1="30" x2="21" y2="30" stroke="#0c3268" stroke-width="2"/></svg></span></div><h3>"Things to Think About Checklist"</h3><p>View our calendar on the left and pick an oppointment time that works best for you.</p></div>
    <div class="step"><div class="ring"><span><svg width="44" height="40" viewBox="0 0 44 40"><rect x="3" y="5" width="38" height="32" rx="3" fill="none" stroke="#0c3268" stroke-width="2.5"/><line x1="3" y1="13" x2="41" y2="13" stroke="#0c3268" stroke-width="2.5"/><rect x="10" y="18" width="7" height="6" fill="none" stroke="#0c3268" stroke-width="2"/><rect x="19" y="18" width="7" height="6" fill="none" stroke="#0c3268" stroke-width="2"/><rect x="28" y="18" width="7" height="6" fill="none" stroke="#0c3268" stroke-width="2"/></svg></span></div><h3>Appointment</h3><p>One of our project managers will meet with you to discuss the project. At this initial stage we will be taking</p></div>
  </div>
</section>

<section class="articles">
  <div class="intro">
    <div class="h-serif">Helpful Articles</div>
    <h2>Our News Feed<br>Articles &amp; tips</h2>
    <p>Lorem Ipsum is simply dummy text of the printing and typesetting industry. Lorem Ipsum has been the industry's</p>
    <a>View All News &nbsp;⟶</a>
  </div>
  <div class="post a"><div class="img" role="img" aria-label="White bathroom with glass shower and tub"></div><div class="meta"><span><i></i>27 Feb ,2021</span><span><i></i>Comments</span></div><h3>Without the right planning, a promising home remodeling project could turn</h3></div>
  <div class="post b"><div class="img" role="img" aria-label="Spacious bathroom with large windows and tub"></div><div class="meta"><span><i></i>27 Feb ,2021</span><span><i></i>Comments</span></div><h3>Without the right planning, a promising home remodeling project could turn</h3></div>
</section>

<footer class="footer">
  <h2 class="sec-title">Other Questions?</h2>
  <div class="contact l"><div class="c"><svg width="38" height="38" viewBox="0 0 24 24"><path d="M6.6 10.8a15 15 0 0 0 6.6 6.6l2.2-2.2a1 1 0 0 1 1-.25 11 11 0 0 0 3.6.6 1 1 0 0 1 1 1V20a1 1 0 0 1-1 1A17 17 0 0 1 3 4a1 1 0 0 1 1-1h3.5a1 1 0 0 1 1 1 11 11 0 0 0 .6 3.6 1 1 0 0 1-.25 1z" fill="none" stroke="#0c3268" stroke-width="1.6"/></svg></div><div><small>Contact us</small><b>555-014-2290</b></div></div>
  <div class="contact r"><div class="c"><svg width="40" height="36" viewBox="0 0 40 36"><circle cx="20" cy="11" r="6" fill="none" stroke="#0c3268" stroke-width="2"/><path d="M8 33c0-7 5-12 12-12s12 5 12 12" fill="none" stroke="#0c3268" stroke-width="2"/></svg></div><div><small>Reach out to our</small><b>Support Team</b></div></div>
  <hr>
  <div class="brand"><span class="mark"></span>PLUMVANTA</div>
  <div class="fsocial"><span></span><span></span><span></span><span></span></div>
  <div class="col s"><h4>Services</h4><ul><li>- Basement Finishing</li><li>- Bathroom Remodeling</li><li>- Handyman</li><li>- Kitchen Remodeling</li><li>- Window Replacement</li><li>- Whole Home</li><li>-Remodeling</li></ul></div>
  <div class="col a"><h4>Service Areas</h4><ul><li>- Ankeny, IA</li><li>- Des Moines, IA</li><li>- Clive, IA</li><li>- Johnston, IA</li><li>- Urbandale, IA</li><li>- Waukee, IA</li><li>- West Des Moines, IA</li></ul></div>
  <div class="copy">Copyright ©2021 Plumvanta All Rights Reserved</div>
</footer>

</body>
</html>
```